"Pause. Pivot. Prosper." Empowerment Book Cover

Hello, I need a hot, trendy, and contemporary book cover designed for my first book called "Pause. Pivot. Prosper. -- 365 Bold Confidence Notes for Anyone Seeking to Pause, Pivot, and Prosper Across Career & Personal Dreams."
This is my first book and I am really wanting to launch my brand with it... it would be awesome to match the inside/outside branding of the book. So we can either create the book cover to match the book guts, or update the book guts to match the cover.
Lastly, I just got a professional photoshoot done last week so we can use one of those images, or we can go with a different idea/style for the cover. The body of the book is attached. All questions welcomed, happy designing!
Target Market(s)
Gen Z, Millennials and Gen X.
Industry/Entity Type
Personal Development.
Requirements
Must have
- It must stand out and be different from other typical book covers.
Nice to have
- Success, Inspiration, Motivation, Mindset, Growth.
Should not have
- Clipart, stock art, stock look and feel.

```html
<!DOCTYPE html>
<html lang="en">
<head>
<meta charset="utf-8">
<title>Pause. Pivot. Prosper. — Samir Qadri</title>
<link rel="stylesheet" href="https://fonts.googleapis.com/css2?family=Mulish:wght@800&family=Questrial&display=swap">
<style>
  :root {
    --bg-deep: #07090d;
    --bg-mid: #1a222b;
    --bg-light: #5f6b78;
    --navy: #243a78;
    --navy-deep: #16244d;
    --teal-light: #6dd9c9;
    --teal-mid: #1cb99f;
    --teal-deep: #00a98d;
    --text-white: #ffffff;
    --shadow: #05070a;
  }
  html, body {
    margin: 0;
    padding: 0;
    width: 800px;
    height: 1200px;
    overflow: hidden;
    background: var(--bg-deep);
  }
  .cover {
    position: relative;
    width: 800px;
    height: 1200px;
    overflow: hidden;
    background: linear-gradient(95deg, var(--bg-deep) 0%, #10161d 35%, var(--bg-mid) 100%);
  }
  .photo-area {
    position: absolute;
    inset: 0;
    background:
      radial-gradient(ellipse 420px 520px at 800px 120px, var(--bg-light) 0%, rgba(95,107,120,0.4) 50%, transparent 100%),
      linear-gradient(180deg, transparent 0%, rgba(36,58,120,0.35) 45%, rgba(22,36,77,0.55) 100%),
      linear-gradient(90deg, transparent 0%, transparent 30%, rgba(36,58,120,0.45) 70%, rgba(22,36,77,0.5) 100%);
  }
  .title {
    position: absolute;
    left: 56px;
    top: 0;
    margin: 0;
    font-family: "Questrial", "Century Gothic", sans-serif;
    font-weight: 400;
    font-size: 158px;
    letter-spacing: -2px;
    line-height: 1;
  }
  .title-line {
    position: absolute;
    left: 0;
    white-space: nowrap;
    text-shadow: 3px 3px 0 var(--shadow);
  }
  .title-line--pause { top: 229px; color: var(--teal-light); }
  .title-line--pivot { top: 402px; color: var(--teal-mid); }
  .title-line--prosper { top: 582px; color: var(--teal-deep); }
  .subtitle {
    position: absolute;
    left: 58px;
    top: 752px;
    width: 700px;
    margin: 0;
    font-family: "Mulish", "Century Gothic", sans-serif;
    font-weight: 800;
    font-size: 29px;
    line-height: 46px;
    color: var(--text-white);
    text-shadow: 1px 1px 2px rgba(0,0,0,0.5);
  }
  .author {
    position: absolute;
    left: 54px;
    top: 1034px;
    margin: 0;
    font-family: "Questrial", "Century Gothic", sans-serif;
    font-weight: 400;
    font-size: 104px;
    line-height: 1;
    color: var(--teal-light);
    white-space: nowrap;
  }
</style>
</head>
<body>
  <main class="cover">
    <div class="photo-area" role="img" aria-label="Space for the author's studio portrait photograph in a navy suit against a dark grey backdrop"></div>

    <h1 class="title">
      <span class="title-line title-line--pause">Pause.</span>
      <span class="title-line title-line--pivot">Pivot.</span>
      <span class="title-line title-line--prosper">Prosper.</span>
    </h1>

    <p class="subtitle">365 Bold Confidence Notes for Anyone<br>Seeking to Pause, Pivot, and Prosper<br>Across Career &amp; Personal Dreams.</p>

    <p class="author">Samir Qadri</p>
  </main>
</body>
</html>
```